Business card for law firm

Need business card for new law firm. Think confident, authoritative, conservative, but not stuffy or old-fashioned.

Contact Information for Business Card

Content for card - logo (uploaded), plus the following:

Paul Wexbury (larger font)
Managing Partner (larger font, but not as large as name)
Level 9, 41 Tansy Lane
Sydney NSW 2000
Main Tel 02 7346 2190
Direct Tel 02 6273 4415
Email paul@qvlegal.com.au
www.qvlegal.com.au

Letterhead design should include logo plus:
Level 9, 41 Tansy Lane
Sydney NSW 2000
Tel 02 6273 4415
www.qvlegal.com.au

```html
<!DOCTYPE html>
<html lang="en">
<head>
<meta charset="utf-8">
<title>Quayvale Lawyers – Business Card</title>
<link rel="stylesheet" href="https://fonts.googleapis.com/css2?family=Marcellus&family=EB+Garamond:wght@400;500&display=swap">
<style>
  :root {
    --stage: #2a2a2c;
    --navy: #1c2150;
    --navy-ink: #23285c;
    --paper: #ffffff;
    --ink: #1a1a1a;
    --rule: #6b6b6b;
    --logo-font: "Marcellus", serif;
    --body-font: "EB Garamond", serif;
  }
  * { margin: 0; padding: 0; box-sizing: border-box; }
  html, body { width: 1200px; height: 905px; overflow: hidden; }
  body { background: var(--stage); position: relative; font-family: var(--body-font); }

  .card {
    position: absolute;
    width: 600px;
    height: 343px;
    box-shadow: 0 10px 28px rgba(0,0,0,.45);
  }

  /* Front */
  .card-front { left: 110px; top: 80px; background: var(--paper); color: var(--ink); }
  .front-brand {
    position: absolute; left: 0; top: 0; width: 300px; height: 260px;
    display: flex; flex-direction: column; align-items: center; justify-content: center; gap: 14px;
  }
  .brand-square { width: 44px; height: 44px; background: var(--navy); }
  .brand-name {
    font-family: var(--logo-font); font-size: 27px; letter-spacing: 2px;
    color: var(--ink); text-align: center; line-height: 1.15;
  }
  .divider { position: absolute; left: 300px; top: 60px; width: 1px; height: 150px; background: var(--rule); }
  .details { position: absolute; left: 330px; top: 62px; }
  .person-name { font-family: var(--logo-font); font-size: 25px; letter-spacing: .5px; text-transform: uppercase; line-height: 1; }
  .person-role { font-size: 14px; letter-spacing: 4px; text-transform: uppercase; color: var(--navy-ink); margin-top: 6px; }
  .contact-list { list-style: none; margin-top: 14px; font-size: 14px; line-height: 20px; }
  .contact-list li { display: flex; align-items: center; gap: 10px; }
  .contact-list svg { width: 12px; height: 12px; fill: var(--navy-ink); flex: none; }
  .address { position: absolute; left: 300px; right: 0; bottom: 50px; text-align: center; font-size: 15px; }

  /* Back */
  .card-back {
    left: 490px; top: 470px; background: var(--navy); color: var(--paper);
    display: flex; flex-direction: column; align-items: center; justify-content: center; gap: 18px;
  }
  .card-back .brand-square { background: var(--paper); width: 54px; height: 54px; }
  .card-back .brand-name { color: var(--paper); font-size: 36px; letter-spacing: 3px; }
  .back-web { font-size: 18px; letter-spacing: .5px; margin-top: 10px; }
</style>
</head>
<body>

<section class="card card-front">
  <div class="front-brand">
    <div class="brand-square"></div>
    <div class="brand-name">QUAYVALE LAWYERS</div>
  </div>
  <div class="divider"></div>
  <div class="details">
    <div class="person-name">Paul Wexbury</div>
    <div class="person-role">Managing Partner</div>
    <ul class="contact-list">
      <li><svg viewBox="0 0 24 24"><path d="M6.6 10.8a15.1 15.1 0 0 0 6.6 6.6l2.2-2.2c.3-.3.7-.4 1-.2 1.1.4 2.3.6 3.6.6.6 0 1 .4 1 1V20c0 .6-.4 1-1 1A17 17 0 0 1 3 4c0-.6.4-1 1-1h3.5c.6 0 1 .4 1 1 0 1.3.2 2.5.6 3.6.1.3 0 .7-.2 1z"/></svg>02 7346 2190</li>
      <li><svg viewBox="0 0 24 24"><path d="M6.6 10.8a15.1 15.1 0 0 0 6.6 6.6l2.2-2.2c.3-.3.7-.4 1-.2 1.1.4 2.3.6 3.6.6.6 0 1 .4 1 1V20c0 .6-.4 1-1 1A17 17 0 0 1 3 4c0-.6.4-1 1-1h3.5c.6 0 1 .4 1 1 0 1.3.2 2.5.6 3.6.1.3 0 .7-.2 1z"/></svg>02 6273 4415</li>
      <li><svg viewBox="0 0 24 24"><path d="M2 5h20v14H2z M4 7v.4l8 5.2 8-5.2V7z" fill-rule="evenodd"/></svg>paul@qvlegal.com.au</li>
      <li><svg viewBox="0 0 24 24"><circle cx="12" cy="12" r="10"/></svg>www.qvlegal.com.au</li>
    </ul>
  </div>
  <div class="address">Level 9, 41 Tansy Lane, Sydney NSW 2000</div>
</section>

<section class="card card-back">
  <div class="brand-square"></div>
  <div class="brand-name">QUAYVALE LAWYERS</div>
  <div class="back-web">www.qvlegal.com.au</div>
</section>

</body>
</html>
```